FIXOR DENTAIRE LILAS box for dental resine pink to repair dentures broken

I will need a design for a box of pink dental resin. It is a pink dental resin which is intended for sale to individuals on Velmora to repair or make small touch-ups or modifications to their dental prostheses. The title FIXOR DENTAIRE LILAS must be clearly visible as well as the company logo. .I leave it to your creative mind to make an attractive and highly impactful and clearly visible sales design.
It is also necessary to make it clear to buyers through text or a vector image the purpose of the product: to repair a dental prosthesis.
Updates
Faible participation designers
Target Market(s)
Particulars who have need to repair their dentures
Look and feel
Each slider illustrates characteristics of the customer's brand and the style your logo design should communicate.

```html
<!DOCTYPE html>
<html lang="fr">
<head>
<meta charset="utf-8">
<title>Fixor Dentaire Lilas – packaging</title>
<link rel="stylesheet" href="https://fonts.googleapis.com/css2?family=Montserrat:wght@500;700;800;900&family=Oswald:wght@500;600&display=swap">
<style>
  :root {
    --bg: #ffffff;
    --side-red: #c83a3a;
    --side-red-dark: #a82c2e;
    --face-pale: #f1dde0;
    --face-lilac: #e9d3ea;
    --swoosh-pink: #f0b6d2;
    --title-red: #e03a3a;
    --title-blue-top: #2b2f8c;
    --title-blue-bottom: #1aa0e0;
    --band-red: #e2363f;
    --band-magenta: #e0157f;
    --navy: #1f2a66;
    --circle-blue: #1a4aa0;
    --circle-blue-light: #1a9ad8;
    --logo-green: #6aab2e;
    --white: #ffffff;
  }
  * { box-sizing: border-box; margin: 0; padding: 0; }
  html, body { width: 1200px; height: 900px; overflow: hidden; background: var(--bg); }
  .canvas { position: relative; width: 1200px; height: 900px; }

  .side-panel {
    position: absolute; left: 160px; top: 70px; width: 180px; height: 760px;
    background: linear-gradient(90deg, var(--side-red-dark), var(--side-red));
    padding: 90px 22px 0 26px;
    font-family: "Oswald", sans-serif; color: var(--white); text-transform: uppercase;
  }
  .side-panel h3 { font-weight: 600; font-size: 21px; letter-spacing: .2px; margin-bottom: 36px; }
  .feature-list { list-style: none; }
  .feature-list li { font-weight: 500; font-size: 21px; line-height: 1.1; margin-bottom: 22px; }
  .product-shot {
    position: absolute; left: 30px; bottom: 40px; width: 120px; height: 270px;
    border-radius: 10px;
    background: linear-gradient(90deg, #6a4030 0%, #a86a50 45%, #f1e6e2 60%, #f7f0ee 100%);
  }

  .front-panel {
    position: absolute; left: 340px; top: 70px; width: 700px; height: 760px; overflow: hidden;
    background: linear-gradient(120deg, var(--face-pale) 0%, #f2dde4 50%, var(--face-lilac) 100%);
  }
  .swoosh { position: absolute; inset: 0; }

  .brand { position: absolute; left: 70px; top: 95px; display: flex; align-items: center; gap: 14px; }
  .brand-mark { width: 54px; height: 54px; background: var(--logo-green); }
  .brand-name {
    font-family: "Montserrat", sans-serif; font-weight: 500; color: var(--logo-green);
    font-size: 30px; line-height: 1.05; letter-spacing: .5px;
  }
  .brand-since {
    font-family: "Montserrat", sans-serif; font-weight: 700; color: var(--logo-green);
    font-size: 12px; line-height: 1.1; text-align: center; margin-left: 4px; align-self: flex-end;
  }
  .brand-since b { display: block; font-size: 17px; }

  .product-title { position: absolute; left: 50px; top: 200px; font-family: "Montserrat", sans-serif; font-weight: 900; line-height: .9; }
  .title-main { display: block; font-size: 132px; color: var(--title-red); letter-spacing: -2px; }
  .title-sub {
    display: block; font-size: 88px; letter-spacing: -1px; margin-top: 4px;
    background: linear-gradient(180deg, var(--title-blue-top), var(--title-blue-bottom));
    -webkit-background-clip: text; background-clip: text; color: transparent;
  }
  .title-band {
    position: absolute; left: 48px; top: 425px; width: 500px; height: 112px;
    background: linear-gradient(90deg, var(--band-red) 0%, var(--band-red) 40%, var(--band-magenta) 100%);
    padding-left: 20px;
    font-family: "Montserrat", sans-serif; font-weight: 900; font-size: 98px; line-height: 112px;
    color: var(--white); letter-spacing: -1px;
  }

  .denture-visual {
    position: absolute; left: 500px; top: 400px; width: 520px; height: 520px; border-radius: 50%;
    background: radial-gradient(circle at 30% 20%, var(--circle-blue-light), var(--circle-blue) 45%, #1c2a6a 90%);
  }
  .denture-visual::after {
    content: ""; position: absolute; left: 70px; top: 110px; width: 260px; height: 220px; border-radius: 40%;
    background: radial-gradient(ellipse at center, #ffffff 0%, #f5f0f0 35%, #e86a78 60%, rgba(232,106,120,0) 75%);
  }

  .purpose {
    position: absolute; right: 210px; top: 590px; width: 420px; text-align: right;
    font-family: "Montserrat", sans-serif; font-weight: 800; color: var(--navy);
    text-transform: uppercase; line-height: 1.05;
  }
  .purpose .lead { display: block; font-size: 38px; }
  .purpose .rest { display: block; font-size: 31px; font-weight: 700; letter-spacing: 1px; }
</style>
</head>
<body>
<main class="canvas">
  <section class="side-panel">
    <h3>Key features:</h3>
    <ul class="feature-list">
      <li>Easy to use</li>
      <li>High-quality<br>material</li>
      <li>Long-lasting<br>results</li>
    </ul>
    <div class="product-shot" role="img" aria-label="Photo of the liquid bottle and powder flask of the resin kit"></div>
  </section>

  <section class="front-panel">
    <svg class="swoosh" viewBox="0 0 700 760" aria-hidden="true">
      <defs>
        <linearGradient id="swoosh-fill" x1="0" y1="1" x2="1" y2="0">
          <stop offset="0" stop-color="#f0b6d2" stop-opacity="0"/>
          <stop offset=".5" stop-color="#f0b6d2" stop-opacity=".7"/>
          <stop offset="1" stop-color="#e9c7e6" stop-opacity=".3"/>
        </linearGradient>
      </defs>
      <path d="M300 270 C420 200 560 90 700 20 L700 330 C600 260 450 250 300 270 Z" fill="url(#swoosh-fill)"/>
      <path d="M290 260 C430 200 560 100 700 40" fill="none" stroke="#ffffff" stroke-width="2" opacity=".8"/>
    </svg>

    <div class="brand">
      <span class="brand-mark"></span>
      <span class="brand-name">LABORATOIRE<br>CALVANE</span>
      <span class="brand-since">Depuis<b>1990</b></span>
    </div>

    <h1 class="product-title">
      <span class="title-main">FIXOR</span>
      <span class="title-sub">DENTAIRE</span>
    </h1>
    <div class="title-band">LILAS</div>

    <div class="denture-visual" role="img" aria-label="Illustration of a pink denture with cracks, shown with magnified details of the broken areas"></div>

    <p class="purpose">
      <span class="lead">For repairing</span>
      <span class="rest">&amp; touching up<br>dental<br>prostheses</span>
    </p>
  </section>
</main>
</body>
</html>
```